Business Card Design

I am a Accounting/Bookkeeping company.  As a sideline, I am also a Notary so I would like that somewhere, either in front or perhaps the backside for the notary business.
I found a standard card I really like but didn't like the "little man" standing on the scale.
I love the colors so I am wondering if you would be able to duplicate this without the man and perhaps money or something appropriate on this side of scale
I also need help on the font.  I tend to like feminine styles but am told they are too hard to read.

Target Market(s)
Small businesses, Individuals
Industry/Entity Type
Business
Contact Information for Business Card
The Tidy Ledgerhouse
Balancing your books is our specialty
Marisol (Perkins) Dellavanti
Accounting Associate
Certified LedgerLoom TaxGuide
Notary Public
Serving Sonoma County                            707-555-3142
marisol.dellavanti@mailvexa.com

Requirements
Must have
- I would like a glossy card

```html
<!DOCTYPE html>
<html lang="en">
<head>
<meta charset="utf-8">
<title>The Tidy Ledgerhouse — Business Card</title>
<link rel="stylesheet" href="https://fonts.googleapis.com/css2?family=Merriweather:wght@400;700&display=swap">
<style>
  :root {
    --page-bg: #ececec;
    --card-gold: #d8cc6c;
    --card-gold-light: #e0d57e;
    --ink: #1c1a12;
    --scale-dark: #151510;
    --scale-mid: #4a4630;
    --shadow: rgba(0, 0, 0, 0.18);
  }
  html, body {
    margin: 0;
    padding: 0;
    width: 1200px;
    height: 972px;
    overflow: hidden;
    background: var(--page-bg);
  }
  .canvas {
    position: relative;
    width: 1200px;
    height: 972px;
  }
  .business-card {
    position: absolute;
    left: 100px;
    top: 200px;
    width: 1000px;
    height: 572px;
    background: linear-gradient(160deg, var(--card-gold-light), var(--card-gold) 55%);
    box-shadow: 0 10px 30px var(--shadow);
    font-family: "Merriweather", Georgia, serif;
    color: var(--ink);
  }
  .scale-artwork {
    position: absolute;
    left: 560px;
    top: 34px;
    width: 380px;
    height: 210px;
    border-radius: 6px;
    background: linear-gradient(180deg, var(--scale-mid), var(--scale-dark));
    opacity: 0.85;
  }
  .brand-name {
    position: absolute;
    left: 60px;
    top: 222px;
    margin: 0;
    font-size: 33px;
    font-weight: 700;
  }
  .tagline {
    position: absolute;
    left: 96px;
    top: 272px;
    margin: 0;
    font-size: 19px;
    font-weight: 400;
  }
  .contact-person {
    position: absolute;
    left: 78px;
    top: 340px;
  }
  .person-name {
    margin: 0 0 8px;
    font-size: 24px;
    font-weight: 700;
  }
  .person-role {
    margin: 0 0 6px 22px;
    font-size: 20px;
    font-weight: 400;
  }
  .person-credential {
    margin: 0 0 0 44px;
    font-size: 20px;
    font-weight: 400;
  }
  .service-area {
    position: absolute;
    left: 60px;
    top: 500px;
    margin: 0;
    font-size: 20px;
  }
  .contact-line {
    position: absolute;
    right: 50px;
    display: flex;
    align-items: center;
    gap: 10px;
    font-size: 20px;
  }
  .contact-line svg { width: 20px; height: 20px; }
  .contact-phone { top: 262px; }
  .contact-email { top: 320px; }
</style>
</head>
<body>
<div class="canvas">
  <article class="business-card">
    <div class="scale-artwork" role="img" aria-label="Illustration of a balance scale with a stack of money on one pan"></div>

    <h1 class="brand-name">The Tidy Ledgerhouse</h1>
    <p class="tagline">Balancing your Books is our Specialty</p>

    <div class="contact-person">
      <p class="person-name">Marisol (Perkins) Dellavanti</p>
      <p class="person-role">Accounting Associate</p>
      <p class="person-credential">Certified LedgerLoom TaxGuide Notary Public</p>
    </div>

    <p class="service-area">Serving Sonoma County</p>

    <div class="contact-line contact-phone">
      <svg viewBox="0 0 20 20" aria-hidden="true">
        <circle cx="10" cy="10" r="10" fill="var(--ink)"/>
        <path d="M7 5.5l2 2-1 1.2c.6 1.3 1.5 2.2 2.8 2.8l1.2-1 2 2-1.3 1.5c-3.3-.4-6.3-3.4-6.7-6.7z" fill="var(--card-gold)"/>
      </svg>
      <span>707-555-3142</span>
    </div>
    <div class="contact-line contact-email">
      <svg viewBox="0 0 20 20" aria-hidden="true">
        <circle cx="10" cy="10" r="9" fill="none" stroke="var(--ink)" stroke-width="1.8"/>
        <rect x="5" y="6.5" width="10" height="7" fill="none" stroke="var(--ink)" stroke-width="1.4"/>
        <path d="M5 6.5l5 4 5-4" fill="none" stroke="var(--ink)" stroke-width="1.4"/>
      </svg>
      <span>marisol.dellavanti@mailvexa.com</span>
    </div>
  </article>
</div>
</body>
</html>
```